Business card design needed

We are a wine business involved in winemaking, broking and packaging on behalf of clients globally with the majority being Asian. The design should be quite traditional and classic with some red used, font used should be easily read.

Target Market(s)

Trade customers other business owners

Industry/Entity Type

Business

Contact Information for Business Card

Rosalind Thwaite
Meridale Wine Collective
PO Box 738, Fenwick Vale
South Australia 5187
Phone: +61 (0)455 982 317
Email: kvcellars@brightmail.example

Logo styles of interest
Lettermark Logo

```html
<!DOCTYPE html>
<html lang="en">
<head>
<meta charset="utf-8">
<title>Meridale Wine Collective – Business Card</title>
<link href="https://fonts.googleapis.com/css2?family=Sorts+Mill+Goudy&family=Playfair+Display:wght@700&display=swap" rel="stylesheet">
<style>
  :root {
    --page: #ffffff;
    --orange-deep: #b9531c;
    --orange-mid: #d9731f;
    --orange-glow: #f5ad22;
    --gold-line: #f6e21a;
    --wall-light: #d9bb82;
    --wall-mid: #a7793e;
    --bottle-dark: #3a200d;
    --text-light: #fff8ec;
  }
  html, body {
    margin: 0;
    width: 1200px;
    height: 1149px;
    overflow: hidden;
    background: var(--page);
  }
  .business-card {
    position: absolute;
    left: 302px;
    top: 397px;
    width: 611px;
    height: 344px;
    overflow: hidden;
    background:
      radial-gradient(ellipse 320px 260px at 230px 110px, var(--orange-glow) 0%, var(--orange-mid) 55%, var(--orange-deep) 100%);
    box-shadow: inset 0 0 0 1px rgba(90, 40, 10, 0.5);
  }
  .photo-panel {
    position: absolute;
    inset: 0;
    width: 611px;
    height: 344px;
  }
  .brand-name {
    position: absolute;
    left: 24px;
    top: 40px;
    width: 300px;
    margin: 0;
    font-family: "Playfair Display", Georgia, serif;
    font-weight: 700;
    font-size: 36px;
    line-height: 1.12;
    color: var(--text-light);
    text-align: center;
  }
  .contact-details {
    position: absolute;
    left: 31px;
    top: 226px;
    margin: 0;
    font-family: "Sorts Mill Goudy", Georgia, serif;
    font-style: normal;
    font-size: 15px;
    line-height: 21px;
    color: var(--text-light);
  }
  .contact-details .phone,
  .contact-details .email {
    display: block;
    line-height: 17px;
  }
  .contact-details .phone { margin-top: 2px; }
</style>
</head>
<body>
  <div class="business-card">
    <svg class="photo-panel" viewBox="0 0 611 344" aria-hidden="false">
      <defs>
        <linearGradient id="cellarTones" x1="0" y1="0" x2="1" y2="0.3">
          <stop offset="0" stop-color="var(--wall-light)"/>
          <stop offset="0.45" stop-color="var(--wall-mid)"/>
          <stop offset="1" stop-color="var(--bottle-dark)"/>
        </linearGradient>
      </defs>
      <path role="img" aria-label="Photograph of a glass of red wine beside bottles of white and red wine against a warm cream wall"
            d="M279,344 C330,300 380,120 470,60 C530,25 580,20 611,18 L611,344 Z"
            fill="url(#cellarTones)"/>
      <path d="M279,344 C330,300 380,120 470,60 C530,25 580,20 611,18"
            fill="none" stroke="var(--gold-line)" stroke-width="3"/>
    </svg>

    <h1 class="brand-name">Meridale<br>Wine Collective</h1>

    <address class="contact-details">
      Rosalind Thwaite Meridale Wine<br>
      Collective, PO Box 738, Fenwick Vale<br>
      South Australia 5187
      <span class="phone">Phone: +61-(0)-455-982-317</span>
      <span class="email">Email: kvcellars@brightmail.example</span>
    </address>
  </div>
</body>
</html>
```